Commercial facility maintenance

I need a card design that helps my salesmen make contact with new clients, our product is facility maintenance and heavy industrial maintenance

```html
<!DOCTYPE html>
<html lang="en">
<head>
<meta charset="utf-8">
<title>Northgate Millwrights LLC – Business Card</title>
<link rel="stylesheet" href="https://fonts.googleapis.com/css2?family=Alfa+Slab+One&family=Michroma&family=Arimo:wght@400&display=swap">
<style>
  :root {
    --bg: #2a2a2b;
    --brand-red: #9c1f2e;
    --charcoal: #3b3b3d;
    --white: #ffffff;
    --paper: #ececec;
    --ink: #2f2f31;
  }
  * { box-sizing: border-box; margin: 0; padding: 0; }
  html, body { width: 1200px; height: 689px; overflow: hidden; background: var(--bg); }
  .stage { position: relative; width: 1200px; height: 689px; }

  .card {
    position: absolute; top: 190px; width: 540px; height: 309px;
    border-radius: 16px; overflow: hidden;
  }

  /* Front */
  .card--front { left: 40px; background: var(--paper); }
  .front__photo {
    position: absolute; inset: 0;
    background: linear-gradient(135deg, #f4f4f4 0%, #dcdcdc 45%, #e8e2d2 70%, #f0f0f0 100%);
  }
  .front__mark {
    position: absolute; left: 50%; top: 116px; transform: translate(-50%, -50%);
    display: flex; flex-direction: column; align-items: center; gap: 14px;
  }
  .front__dot {
    width: 92px; height: 92px; border-radius: 50%;
    background: var(--white); border: 4px solid var(--ink);
  }
  .front__name {
    font-family: "Michroma", sans-serif; font-size: 17px; color: var(--ink);
    letter-spacing: 1px; text-align: center; line-height: 1.4;
  }
  .front__tagline {
    position: absolute; left: 0; right: 0; bottom: 34px; text-align: center;
    font-family: "Michroma", sans-serif; font-size: 11px; letter-spacing: 1px;
    color: var(--ink);
  }
  .front__tagline .accent { color: var(--brand-red); }

  /* Back */
  .card--back { left: 620px; background: var(--brand-red); }
  .back__panel {
    position: absolute; right: 0; top: 0; width: 170px; height: 100%;
    background: var(--charcoal);
  }
  .back__disc {
    position: absolute; right: 40px; top: -6px; width: 210px; height: 210px;
    border-radius: 50%; background: var(--white); border: 26px solid var(--charcoal);
  }
  .back__content { position: absolute; left: 30px; top: 40px; color: var(--white); }
  .back__brand {
    font-family: "Michroma", sans-serif; font-size: 16px; line-height: 1.35;
    letter-spacing: 1px;
  }
  .back__motto {
    font-family: "Michroma", sans-serif; font-size: 7.5px; letter-spacing: .6px;
    margin-top: 8px; padding-top: 6px; border-top: 1.5px solid var(--white); width: 220px;
  }
  .back__person {
    font-family: "Alfa Slab One", serif; font-size: 22px; margin-top: 26px; letter-spacing: .5px;
  }
  .back__role { font-family: "Arimo", sans-serif; font-size: 12px; margin-top: 2px; }
  .contact { list-style: none; margin-top: 18px; font-family: "Arimo", sans-serif; font-size: 11px; line-height: 1.45; }
  .contact li { display: flex; align-items: flex-start; gap: 8px; }
  .contact svg { width: 10px; height: 10px; margin-top: 3px; flex: none; fill: var(--white); }
</style>
</head>
<body>
<main class="stage">
  <section class="card card--front">
    <div class="front__photo" role="img" aria-label="Faded photograph of industrial rigging: chains, hoists and clamps on a steel wall"></div>
    <div class="front__mark">
      <div class="front__dot"></div>
      <p class="front__name">NORTHGATE<br>MILLWRIGHTS LLC.</p>
    </div>
    <p class="front__tagline">PRECISION. EXPERIENCE. MECHANICAL <span class="accent">SOLUTIONS THAT LAST.</span></p>
  </section>

  <section class="card card--back">
    <div class="back__panel"></div>
    <div class="back__disc"></div>
    <div class="back__content">
      <p class="back__brand">NORTHGATE<br>MILLWRIGHTS LLC.</p>
      <p class="back__motto">PRECISION. PUNCTUALITY. PROFESSIONALISM.</p>
      <h1 class="back__person">DANIEL REYES</h1>
      <p class="back__role">Founder &amp; CEO</p>
      <ul class="contact">
        <li><svg viewBox="0 0 10 10"><path d="M5 0a3.5 3.5 0 0 0-3.5 3.5C1.5 6 5 10 5 10s3.5-4 3.5-6.5A3.5 3.5 0 0 0 5 0zm0 5a1.5 1.5 0 1 1 0-3 1.5 1.5 0 0 1 0 3z"/></svg>
          <span>Northgate Millwrights LLC<br>Your Street Address Here, City<br>State, Country, ZIP 123</span></li>
        <li><svg viewBox="0 0 10 10"><path d="M2 0l2 2.5-1 1.2a6 6 0 0 0 3.3 3.3l1.2-1L10 8l-1.5 2C4 10 0 6 0 1.5z"/></svg><span>555-014-2290</span></li>
        <li><svg viewBox="0 0 10 10"><path d="M0 2h10v6H0zm1 1l4 3 4-3z"/></svg><span>office@northgatemillwrights.com</span></li>
        <li><svg viewBox="0 0 10 10"><circle cx="5" cy="5" r="4.5"/></svg><span>northgatemillwrights.com</span></li>
      </ul>
    </div>
  </section>
</main>
</body>
</html>
```